BrivoMatex. Lantern for the Steady Growth. Business card

Professional business card for BrivoMatex (Lantern for the Steady Growth)
My rationale: Strategy-> Execution-> Results-> Value that lead to the BrivoMatex name: We put the Lantern for the Steady Growth.
We deliver value to our customers helping them at defining a good strategy (cyan arrow). 90% of well formulated strategies fail due to poor execution so we also consider strategical execution very important (green arrow). Due to the execution we obtain the results (blue arrow). Finally, the results provide feedback to redefine strategy, and the new strategy has to be executed and new results obtained providing new feedback and on and on. It's like a wheel that finally, must create corporate value: value for shareholders, staholders, employees, providers...-

Target Market(s)

CEOs and steering comitees , invewrnent funds

Industry/Entity Type

Business Consultant

Contact Information for Business Card

Tommaso Ferlini
CEO & Founder
tommaso.ferlini@brivomatex.example
Mobile: +34 611.205.938
www.brivomatex.example

Colors

Designer to choose colors to be used in the design.

Requirements
Nice to have
• Nice to hace the words: Strategy, execution, results
• Nice to vave the claim: Lantern for the Steady Growth
• The three colors should be shown:
• cyan for STRATEGY
• green for EXECUTION
• blue for RESULTS
Should not have
• Complete black background

```html
<!DOCTYPE html>
<html lang="en">
<head>
<meta charset="utf-8">
<title>BrivoMatex – Business Card</title>
<link rel="stylesheet" href="https://fonts.googleapis.com/css2?family=Montserrat:wght@400;600;700&family=Roboto:wght@400&display=swap">
<style>
  :root {
    --bg: #d1d2d4;
    --navy: #233e91;
    --green: #8dc63f;
    --cyan: #29abe2;
    --white: #ffffff;
    --ink: #555a62;
  }
  * { box-sizing: border-box; margin: 0; padding: 0; }
  html, body { width: 1200px; height: 900px; overflow: hidden; background: var(--bg); }
  .canvas {
    width: 1200px; height: 900px;
    display: flex; flex-direction: column; align-items: center; justify-content: center; gap: 50px;
  }
  .card {
    position: relative; width: 580px; height: 330px; border-radius: 16px; overflow: hidden;
    box-shadow: 0 6px 16px rgba(0,0,0,.22);
  }
  /* Back side */
  .card--back { background: var(--navy); display: flex; align-items: center; justify-content: center; }
  .brand {
    font-family: "Montserrat", sans-serif; font-weight: 700; letter-spacing: -0.5px;
    display: flex; align-items: center; gap: 14px; white-space: nowrap;
  }
  .brand__dot { width: 18px; height: 18px; border-radius: 50%; background: var(--green); flex: none; }
  .card--back .brand { color: var(--white); font-size: 58px; }
  /* Front side */
  .card--front { background: var(--white); }
  .card--front .brand {
    position: absolute; left: 36px; top: 122px; color: var(--navy); font-size: 29px; gap: 9px;
  }
  .card--front .brand__dot { width: 11px; height: 11px; }
  .divider {
    position: absolute; left: 272px; top: 58px; width: 2px; height: 150px; background: var(--cyan);
  }
  .person { position: absolute; left: 294px; top: 56px; }
  .person__name { font-family: "Montserrat", sans-serif; font-weight: 700; font-size: 21px; color: var(--navy); }
  .person__role { font-family: "Montserrat", sans-serif; font-weight: 600; font-size: 15px; color: var(--green); margin-top: 2px; }
  .contacts { list-style: none; margin-top: 16px; font-family: "Roboto", sans-serif; font-size: 13px; color: var(--ink); }
  .contacts li { display: flex; align-items: center; gap: 8px; height: 21px; white-space: nowrap; }
  .icon { width: 15px; height: 15px; flex: none; }
  .claims {
    position: absolute; left: 160px; top: 246px; display: flex; gap: 22px;
    font-family: "Montserrat", sans-serif; font-size: 17px; color: var(--ink); letter-spacing: .5px;
  }
  .claims span { display: flex; align-items: center; gap: 7px; }
  .claims i { width: 8px; height: 8px; display: inline-block; }
  .claims .s i { background: var(--navy); }
  .claims .e i { background: var(--green); }
  .claims .r i { background: var(--cyan); }
  .band { position: absolute; left: 0; bottom: 0; width: 100%; height: 14px; display: flex; }
  .band__blue { flex: 0 0 64%; background: var(--navy); }
  .band__green { flex: 0 0 22%; background: var(--green); }
  .band__cyan { flex: 1; background: var(--cyan); }
</style>
</head>
<body>
<main class="canvas">
  <section class="card card--back" aria-label="Business card back">
    <div class="brand"><span class="brand__dot"></span>BrivoMatex</div>
  </section>

  <section class="card card--front" aria-label="Business card front">
    <div class="brand"><span class="brand__dot"></span>BrivoMatex</div>
    <div class="divider"></div>
    <div class="person">
      <p class="person__name">Tommaso Ferlini</p>
      <p class="person__role">CEO &amp; Founder</p>
      <ul class="contacts">
        <li>
          <svg class="icon" viewBox="0 0 16 16"><circle cx="8" cy="8" r="8" fill="#233e91"/><path d="M5.2 4.2l1.4-.3.8 2-1 .8a6 6 0 0 0 2.9 2.9l.8-1 2 .8-.3 1.4c-3.9.3-7-2.8-6.6-6.6z" fill="#fff"/></svg>
          +34 611.205.938
        </li>
        <li>
          <svg class="icon" viewBox="0 0 16 16"><circle cx="8" cy="8" r="8" fill="#8dc63f"/><rect x="4" y="5" width="8" height="6" fill="none" stroke="#fff" stroke-width="1.1"/><path d="M4 5l4 3.2L12 5" fill="none" stroke="#fff" stroke-width="1.1"/></svg>
          tommaso.ferlini@brivomatex.example
        </li>
        <li>
          <svg class="icon" viewBox="0 0 16 16"><circle cx="8" cy="8" r="8" fill="#29abe2"/><circle cx="8" cy="8" r="4" fill="none" stroke="#fff" stroke-width="1.1"/><path d="M4 8h8M8 4c-2 2.4-2 5.6 0 8M8 4c2 2.4 2 5.6 0 8" fill="none" stroke="#fff" stroke-width=".9"/></svg>
          www.brivomatex.example
        </li>
      </ul>
    </div>
    <div class="claims">
      <span class="s"><i></i>Strategy</span>
      <span class="e"><i></i>Execution</span>
      <span class="r"><i></i>Results</span>
    </div>
    <div class="band"><span class="band__blue"></span><span class="band__green"></span><span class="band__cyan"></span></div>
  </section>
</main>
</body>
</html>
```